Logo and label lay out for Copper Thistle wines

Wine Bottle label for single vineyard on The Mornington Peninsula, Victoria, Australia
Name of Vineyard is “Copper Thistle”
(A copper Thistle is a common biting ant found in the vineyard.)
The name and vintage of each of the four varieties of wine will need to be included on the label.
We want an instantly recognisable image on the label along with the name Copper Thistle.

Target Market(s)

Quality wine for cafes, restaurants and individual’s wine collection

Industry/Entity Type

Vineyard

Logo Text

Copper Thistle

Logo styles of interest
Emblem Logo
Abstract Logo
Colors

Designer to choose colors to be used in the design.

Requirements
Must have
• Simple yet stylish image, instantly recognisable .
Nice to have
• Possibly a stylistic image of an ant
Should not have
• Not an overly detailed image.

```html
<!DOCTYPE html>
<html lang="en">
<head>
<meta charset="utf-8">
<title>Copper Thistle – Single Vineyard Chardonnay Label</title>
<link rel="stylesheet" href="https://fonts.googleapis.com/css2?family=Josefin+Sans:wght@400;600&display=swap">
<style>
  :root {
    --page-bg: #f2f2f2;
    --label-ink: #0a0a0a;
    --label-paper: #ffffff;
  }
  html, body {
    margin: 0;
    padding: 0;
    width: 960px;
    height: 1200px;
    overflow: hidden;
    background: var(--page-bg);
  }
  .canvas {
    position: relative;
    width: 960px;
    height: 1200px;
  }
  .label {
    position: absolute;
    left: 260px;
    top: 100px;
    width: 440px;
    height: 1000px;
    background: var(--label-ink);
    font-family: "Josefin Sans", "Helvetica Neue", Arial, sans-serif;
    color: var(--label-paper);
  }
  .label-stripes {
    position: absolute;
    left: 0;
    top: 0;
  }
  .brand-mark {
    position: absolute;
    left: 0;
    width: 100%;
    top: 150px;
    display: flex;
    justify-content: center;
    align-items: center;
    gap: 8px;
    font-size: 13px;
    font-weight: 600;
    letter-spacing: 0.2em;
    text-transform: uppercase;
  }
  .brand-mark .mark-dot {
    width: 10px;
    height: 10px;
    border-radius: 50%;
    background: var(--label-paper);
  }
  .wine-name {
    position: absolute;
    left: 38px;
    top: 548px;
    margin: 0;
    color: var(--label-ink);
    font-size: 32px;
    font-weight: 400;
    letter-spacing: 0.55em;
    line-height: 79px;
    text-transform: uppercase;
  }
  .wine-details {
    position: absolute;
    left: 39px;
    top: 780px;
    margin: 0;
    font-size: 20px;
    font-weight: 600;
    letter-spacing: 0.12em;
    line-height: 31px;
    text-transform: uppercase;
  }
  .wine-origin {
    position: absolute;
    left: 39px;
    top: 873px;
    margin: 0;
    font-size: 20px;
    font-weight: 600;
    letter-spacing: 0.1em;
    line-height: 25px;
    text-transform: uppercase;
  }
</style>
</head>
<body>
<main class="canvas">
  <section class="label">
    <svg class="label-stripes" width="440" height="1000" viewBox="0 0 440 1000" aria-hidden="true">
      <rect class="stripe" x="0" y="190" width="440" height="16" fill="var(--label-paper)"/>
      <rect class="stripe" x="0" y="240" width="440" height="31" fill="var(--label-paper)"/>
      <rect class="stripe" x="0" y="314" width="440" height="41" fill="var(--label-paper)"/>
      <rect class="name-panel" x="0" y="402" width="440" height="327" fill="var(--label-paper)"/>
    </svg>
    <div class="brand-mark"><span class="mark-dot"></span>Copper Thistle</div>
    <h1 class="wine-name">Copper<br>Thistle</h1>
    <p class="wine-details">Single Vinyard<br>Chardonnay</p>
    <p class="wine-origin">Mornington Peninsula<br>Wine of Australia</p>
  </section>
</main>
</body>
</html>
```